Tallowfen Capital Group - letterhead

We need a corporate letterhead template (word) and slide show template (PowerPoint) designed for our investment business Tallowfen Capital Group.

Tallowfen Capital Group manages a group of investments in Australia and are after a letterhead template and PowerPoint template that is both creative and professional in design.

Information to be included on the letterhead (word) template is as follows:

Level 4, 318 Marlow Road
Fernlea VIC 3188

t. 03 5127 6618

Please feel free to ask any questions.

Investment

```html
<!DOCTYPE html>
<html lang="en">
<head>
<meta charset="utf-8">
<title>Tallowfen Capital Group – Letterhead</title>
<link rel="stylesheet" href="https://fonts.googleapis.com/css2?family=Questrial&display=swap">
<style>
  :root {
    --backdrop: #ececec;
    --paper: #f7f7f6;
    --brand-blue: #1f6aa5;
    --ink-grey: #5a5d60;
    --shadow: rgba(0, 0, 0, 0.12);
  }
  * { margin: 0; padding: 0; box-sizing: border-box; }
  html, body {
    width: 1200px;
    height: 936px;
    overflow: hidden;
    background: var(--backdrop);
  }
  .canvas {
    position: relative;
    width: 1200px;
    height: 936px;
  }
  .letterhead {
    position: absolute;
    left: 300px;
    top: 44px;
    width: 600px;
    height: 848px;
    background: var(--paper);
    box-shadow: 0 4px 18px var(--shadow);
    font-family: "Questrial", "Century Gothic", sans-serif;
  }
  .letterhead__brand {
    position: absolute;
    left: 62px;
    top: 74px;
    display: flex;
    align-items: center;
    gap: 10px;
  }
  .brand__mark {
    width: 12px;
    height: 12px;
    border-radius: 50%;
    background: var(--brand-blue);
  }
  .brand__name {
    color: var(--brand-blue);
    font-size: 20px;
    letter-spacing: 0.06em;
    text-transform: uppercase;
    white-space: nowrap;
  }
  .letterhead__contact {
    position: absolute;
    right: 40px;
    bottom: 30px;
    font-size: 9px;
    color: var(--ink-grey);
    letter-spacing: 0.02em;
    white-space: nowrap;
  }
  .contact__label {
    color: var(--brand-blue);
    font-weight: 700;
  }
  .letterhead__band {
    position: absolute;
    left: 0;
    right: 0;
    bottom: 0;
    height: 11px;
    background: var(--brand-blue);
  }
</style>
</head>
<body>
  <main class="canvas">
    <article class="letterhead">
      <header class="letterhead__brand">
        <span class="brand__mark"></span>
        <span class="brand__name">Tallowfen Capital Group</span>
      </header>
      <footer class="letterhead__contact">
        Level 4, 318 Marlow Road, Fernlea VIC 3188 &nbsp;·&nbsp; <span class="contact__label">Phone:</span> 03 5127 6618
      </footer>
      <div class="letterhead__band"></div>
    </article>
  </main>
</body>
</html>
```